Seven Quiet Rooms Poster

Seven Quiet Rooms is reaching out to designers, creatives and fans alike to help create an exciting new poster for the film as part of our Fundvaro campaign.

Seven Quiet Rooms is a multi-protagonist, multicultural, humanist drama inspired by the 2008 Mumbai terrorist attacks. Centering on a group of international tourists trapped in their hotel by Islamic fundamentalists, the film aims to explore the key issues facing our society, concerning atheism, religion, religious extremism and humanism.

The film’s poster will be a critical part of a film’s publicity and marketing portfolio and an important resource for the film to take into our festival campaign and distribution talks. We’re looking for a highly polished design that accurately represents the film and matches the standard of the finished film.

We will be uploading some of the best entries to our Chatterbox page for fans to vote on. If you do not wish for your design to appear on the page, please contact us.

You can find our teaser trailer on the Fundvaro link below. We’ve also provided some reference images (found here: http://lnk.example-short.net/Rk4WpZ) and also stills from the film to provide inspiration (found here: http://lnk.example-short.net/Tm8QvB) - how or if you use them is up to you.

Good luck and get designing!

http://www.fundvaro-example.com/projects/seven-quiet-rooms

Please note: Amber Tide Pictures reserves the right to select all promotional material for theatrical release.

Requirements
Must have
• Size: 27" x 40"
Should not have
• Please do not include the credit block on your designs.

```html
<!DOCTYPE html>
<html lang="en">
<head>
<meta charset="utf-8">
<title>Seven Quiet Rooms – Poster</title>
<link rel="stylesheet" href="https://fonts.googleapis.com/css2?family=Jost:wght@400;500&family=Josefin+Sans:wght@400&display=swap">
<style>
  :root {
    --backdrop: #ececec;
    --poster-dark: #2a2724;
    --poster-mid: #4a4743;
    --poster-light: #67645f;
    --ink-pale: #e6e0d8;
    --ink-soft: #d8d0c6;
    --accent-copper: #c9977a;
    --tone-steel: #8a8d94;
    --tone-amber: #b4754c;
    --tone-blush: #c7949a;
    --tone-rose: #a86d72;
    --tone-sand: #c9ab98;
    --tone-slate: #6e7a85;
    --tone-umber: #5b4436;
    --tone-shadow: #3a3430;
  }
  html, body {
    margin: 0;
    padding: 0;
    width: 989px;
    height: 1200px;
    overflow: hidden;
    background: var(--backdrop);
  }
  .poster {
    position: absolute;
    left: 135px;
    top: 128px;
    width: 720px;
    height: 968px;
    overflow: hidden;
  }
  .poster svg { display: block; }
  .review-stars {
    font-family: "Jost", sans-serif;
    font-size: 22px;
    letter-spacing: 2px;
    fill: var(--ink-soft);
  }
  .review-quote {
    font-family: "Josefin Sans", sans-serif;
    font-size: 9.5px;
    fill: var(--ink-soft);
  }
  .title-letter {
    font-family: "Jost", sans-serif;
    font-weight: 500;
    font-size: 172px;
  }
  .director-credit {
    font-family: "Jost", sans-serif;
    font-weight: 500;
    font-size: 12.5px;
    letter-spacing: 2.4px;
    fill: var(--accent-copper);
  }
</style>
</head>
<body>
<main class="poster">
  <svg width="720" height="968" viewBox="0 0 720 968" xmlns="http://www.w3.org/2000/svg">
    <defs>
      <linearGradient id="key-art-tone" x1="0" y1="0" x2="1" y2="0.3">
        <stop offset="0" stop-color="var(--poster-light)"/>
        <stop offset="0.45" stop-color="var(--poster-mid)"/>
        <stop offset="1" stop-color="var(--poster-dark)"/>
      </linearGradient>
      <linearGradient id="fill-warm" x1="0" y1="0" x2="1" y2="1">
        <stop offset="0" stop-color="var(--tone-amber)"/>
        <stop offset="1" stop-color="var(--tone-umber)"/>
      </linearGradient>
      <linearGradient id="fill-blush" x1="0" y1="0" x2="1" y2="1">
        <stop offset="0" stop-color="var(--tone-blush)"/>
        <stop offset="1" stop-color="var(--tone-rose)"/>
      </linearGradient>
      <linearGradient id="fill-cool" x1="0" y1="0" x2="0" y2="1">
        <stop offset="0" stop-color="var(--tone-steel)"/>
        <stop offset="1" stop-color="var(--tone-slate)"/>
      </linearGradient>
    </defs>

    <rect class="key-art" role="img" aria-label="Close-up film still of a woman's face and eye in low, dim light"
          width="720" height="968" fill="url(#key-art-tone)"/>

    <g class="press-quotes">
      <text class="review-stars" x="195" y="93" text-anchor="middle">★★★★★</text>
      <text class="review-quote" text-anchor="middle">
        <tspan x="195" y="121">Donec aliquet leo ut porttitor rhoncus. Suspendisse odio</tspan>
        <tspan x="195" y="134">nulla, finibus fringilla viverra nec, feugiat vel tortor.</tspan>
        <tspan x="195" y="147">- Nightfall Weekly</tspan>
      </text>

      <ellipse class="festival-badge" cx="380" cy="98" rx="42" ry="34" fill="none" stroke="var(--ink-soft)" stroke-width="1.5" opacity="0.8"/>

      <text class="review-stars" x="558" y="93" text-anchor="middle">★★★★★</text>
      <text class="review-quote" text-anchor="middle">
        <tspan x="558" y="121">Interdum et malesuada fames ac ante ipsum primis</tspan>
        <tspan x="558" y="134">in faucibus.</tspan>
        <tspan x="558" y="147">- ReelVerdict.net</tspan>
      </text>
    </g>

    <g class="film-title" role="img" aria-label="Seven Quiet Rooms, letters filled with film stills">
      <text class="title-letter" y="367" text-anchor="middle">
        <tspan x="108" fill="url(#fill-cool)">S</tspan>
        <tspan x="234" fill="url(#fill-warm)">E</tspan>
        <tspan x="360" fill="var(--tone-umber)">V</tspan>
        <tspan x="486" fill="url(#fill-blush)">E</tspan>
        <tspan x="612" fill="var(--tone-sand)" fill-opacity="0.85">N</tspan>
      </text>
      <text class="title-letter" y="544" text-anchor="middle">
        <tspan x="108" fill="url(#fill-cool)" fill-opacity="0.75">Q</tspan>
        <tspan x="234" fill="url(#fill-blush)">U</tspan>
        <tspan x="360" fill="var(--tone-rose)">I</tspan>
        <tspan x="486" fill="url(#fill-blush)" fill-opacity="0.85">E</tspan>
        <tspan x="612" fill="var(--tone-slate)">T</tspan>
      </text>
      <text class="title-letter" y="720" text-anchor="middle">
        <tspan x="108" fill="var(--tone-umber)" fill-opacity="0.8">R</tspan>
        <tspan x="234" fill="var(--tone-shadow)">O</tspan>
        <tspan x="360" fill="url(#fill-warm)">O</tspan>
        <tspan x="486" fill="var(--tone-shadow)" fill-opacity="0.8">M</tspan>
        <tspan x="612" fill="var(--tone-shadow)" fill-opacity="0.6">S</tspan>
      </text>
    </g>

    <text class="director-credit" x="360" y="811" text-anchor="middle">A FILM BY ALDO FENWICK</text>
  </svg>
</main>
</body>
</html>
```